business card/stationery
See remarks
business card/stationery - Real Estate
Use same font as used in my logo
Whatever you think may look best
Professional
Megan Thistle
Broker Sales Agent
1738 Brambleford Lane Suite 410 Cedarmoor Hollow, CA 90817
Megan@BrindleTerraHomes.com
www.MeganThistleHomes.com
CA DLH #07316925 Office lic CA DLH #06258340

```html
<!DOCTYPE html>
<html lang="en">
<head>
<meta charset="utf-8">
<title>Brindle Terra — Stationery Concepts</title>
<link href="https://fonts.googleapis.com/css2?family=EB+Garamond:wght@500&family=Open+Sans:wght@400;700&family=Great+Vibes&display=swap" rel="stylesheet">
<style>
:root{
  --backdrop:#a7987e;
  --paper:#ffffff;
  --paper-shade:#eeeeee;
  --red:#a3121f;
  --red-deep:#5a0a10;
  --ink:#333333;
  --muted:#8a8a8a;
  --charcoal:#1e1e1e;
}
*{margin:0;padding:0;box-sizing:border-box}
html,body{width:1200px;height:254px;overflow:hidden}
body{background:var(--backdrop);position:relative;font-family:"Open Sans",Arial,sans-serif;color:var(--ink)}
.piece{position:absolute;background:var(--paper);box-shadow:0 1px 3px rgba(0,0,0,.25);overflow:hidden}
.brand{font-family:"EB Garamond",Georgia,serif;font-weight:500;color:var(--red);white-space:nowrap;line-height:1}
.brand.light{color:var(--paper)}
.red-fill{background:radial-gradient(circle at 50% 45%,#c21a2c 0%,var(--red) 35%,var(--red-deep) 100%)}
.band{position:absolute;left:0;right:0;bottom:0;background:linear-gradient(var(--red),var(--red-deep));color:#fff;font-size:1.6px;text-align:center;line-height:2.2px;padding:0.5px 0;white-space:nowrap}
.tiny{font-size:1.8px;line-height:2.4px}
.intro{position:absolute;left:0;top:0;width:62px;height:254px;background:linear-gradient(90deg,#b9ab94,#a7987e)}
.intro .brand{position:absolute;left:15px;top:50px;font-size:8px}
.intro .sub{position:absolute;left:17px;top:61px;font-size:3.4px;color:#5a4c3a}
.card{width:47px;height:29px}
.card .brand{position:absolute;left:3px;top:5px;font-size:4px}
.card .details{position:absolute;left:3px;top:13px;color:#555}
.card .photo{position:absolute;right:4px;top:3px;width:9px;height:12px;background:linear-gradient(#d8c2ae,#b89a83)}
.card .band{height:2.5px}
.letterhead{width:80px;height:101px}
.letterhead .brand{position:absolute;left:5px;top:7px;font-size:5px}
.letterhead .addr{position:absolute;right:4px;top:5px;width:28px;color:#666;font-size:1.5px;line-height:2px}
.letterhead .body{position:absolute;left:6px;top:22px;right:6px;font-size:1.6px;line-height:2.1px;color:#555}
.letterhead .body p{margin-bottom:2px}
.letterhead .sig{font-family:"Great Vibes",cursive;font-size:5px;color:#333;line-height:5px}
.letterhead .band{height:5px;line-height:4px}
.envelope{width:87px;height:37px}
.envelope .brand{position:absolute;left:5px;top:6px;font-size:4.2px}
.envelope .addr{position:absolute;left:5px;top:11px;width:30px;color:#666;font-size:1.4px;line-height:1.9px}
.envelope .band{height:3px}
.flap{position:absolute;left:0;right:0;top:0;height:20px;clip-path:polygon(0 0,100% 0,100% 40%,50% 100%,0 40%)}
.folder{width:126px;height:99px}
.folder .cover{position:absolute;right:0;top:0;width:58px;height:78px;background:var(--paper)}
.folder .cover .brand{position:absolute;left:11px;top:36px;font-size:7px}
.folder .pocket{position:absolute;right:0;bottom:0;width:58px;height:22px}
.fax{width:79px;height:102px}
.fax .brand{position:absolute;left:4px;top:6px;font-size:4.2px}
.fax table{position:absolute;left:4px;right:4px;top:16px;width:71px;border-collapse:collapse;font-size:1.5px}
.fax td{border:0.3px solid #ccc;height:3.6px;padding:0 1px;color:#555}
.fax td.f{background:#eee}
.fax .checks{position:absolute;left:4px;top:36px;font-size:1.5px;color:#555;white-space:nowrap}
.fax .band{height:4px;line-height:3px}
.slip{width:88px;height:36px}
.slip .brand{position:absolute;left:4px;top:7px;font-size:4.5px}
.script{font-family:"Great Vibes",cursive;color:#7a7a7a;white-space:nowrap}
.slip .script{position:absolute;left:20px;top:17px;font-size:7px}
.slip .band{height:3px}
.disc{position:absolute;border-radius:50%;box-shadow:0 1px 3px rgba(0,0,0,.35)}
.disc .hub{position:absolute;left:50%;top:50%;width:34%;height:34%;margin:-17% 0 0 -17%;border-radius:50%;background:var(--backdrop);border:2px solid #fff}
.disc .brand{position:absolute;left:0;right:0;top:19%;text-align:center;font-size:4.2px}
.disc .url{position:absolute;left:0;right:0;bottom:14%;text-align:center;font-size:1.4px;color:#fff}
.magnet{position:absolute;border-radius:50%;box-shadow:0 1px 2px rgba(0,0,0,.4);display:flex;align-items:center;justify-content:center}
.magnet .brand{font-size:3px}
.slide{width:92px;height:70px}
.slide h3{position:absolute;left:5px;top:5px;font-size:3.2px;color:var(--red);font-weight:700}
.slide h4{position:absolute;left:5px;top:9px;font-size:1.8px;color:#555;font-weight:400}
.slide .band{height:4px;line-height:3px}
.slide .col{position:absolute;font-size:1.5px;line-height:2px;color:#555}
.slide .col b{color:var(--red);display:block;font-size:1.9px}
.thumb{position:absolute;top:17px;width:17px;height:16px;background:#6e6e6e}
</style>
</head>
<body>

<section class="intro">
  <div class="brand">Brindle Terra</div>
  <div class="sub">Stationary Concepts</div>
</section>

<article class="piece card" style="left:9px;top:70px">
  <div class="brand">Brindle Terra</div>
  <div class="details tiny">Megan Thistle · Broker<br>(805) 555-0142<br>Megan@BrindleTerraHomes.com<br>CA DLH #07316925</div>
  <div class="photo" role="img" aria-label="Agent portrait photo"></div>
  <div class="band"></div>
</article>

<article class="piece letterhead" style="left:64px;top:15px">
  <div class="brand">Brindle Terra</div>
  <div class="addr">1738 Brambleford Lane Suite 410<br>Cedarmoor Hollow, CA 90817<br>(805) 555-0142<br>Megan@BrindleTerraHomes.com</div>
  <div class="body">
    <p>Date<br><b>Recipient Name</b><br>Company Name<br>Street Address<br>City, State, Zip</p>
    <p>Dear client, thank you for trusting our team with your home search this season. We look forward to guiding every step ahead with care and local insight.</p>
    <p>Our office remains ready to answer any question about listings, offers, inspections or closing timelines. Please reach out whenever it suits you.</p>
    <p>Sincerely,</p>
    <div class="sig">Signature</div>
    <p>Megan Thistle<br>Broker · Sales Agent</p>
  </div>
  <div class="band">1738 Brambleford Lane Suite 410 · www.MeganThistleHomes.com</div>
</article>

<article class="piece letterhead" style="left:148px;top:15px">
  <div class="brand" style="left:30px">Brindle Terra</div>
  <div class="body">
    <p>Date<br><b>Recipient Name</b><br>Company Name<br>Street Address<br>City, State, Zip</p>
    <p>Dear client, thank you for trusting our team with your home search this season. We look forward to guiding every step ahead with care and local insight.</p>
    <p>Our office remains ready to answer any question about listings, offers, inspections or closing timelines. Please reach out whenever it suits you.</p>
    <p>Sincerely,</p>
    <div class="sig">Signature</div>
    <p>Megan Thistle<br>Broker · Sales Agent</p>
  </div>
  <div class="band">Cedarmoor Hollow, CA 90817 · Megan@BrindleTerraHomes.com</div>
</article>

<article class="piece card" style="left:250px;top:41px;width:53px;height:26px">
  <div class="brand">Brindle Terra</div>
  <div class="details tiny">1738 Brambleford Lane<br>(805) 555-0142<br>(805) 555-0187</div>
  <div class="photo" role="img" aria-label="Agent portrait photo"></div>
  <div class="band">www.MeganThistleHomes.com</div>
</article>

<article class="piece envelope" style="left:231px;top:80px">
  <div class="brand">Brindle Terra</div>
  <div class="addr">1738 Brambleford Lane Suite 410<br>Cedarmoor Hollow, CA 90817</div>
  <div class="band"></div>
</article>
<article class="piece envelope" style="left:327px;top:40px;width:90px;height:40px">
  <div class="flap red-fill"></div>
  <div class="band" style="background:none;color:#888;bottom:14px">www.MeganThistleHomes.com</div>
</article>
<article class="piece envelope" style="left:320px;top:80px">
  <div class="flap" style="background:var(--paper-shade)"></div>
  <div class="band" style="background:none;color:#888;bottom:10px">www.MeganThistleHomes.com</div>
</article>

<article class="piece folder red-fill" style="left:422px;top:18px">
  <div class="cover"><div class="brand">Brindle Terra</div>
    <div class="band" style="height:3px"></div></div>
  <div class="pocket red-fill"></div>
  <div class="tiny" style="position:absolute;left:8px;bottom:12px;color:#fff;width:40px">1738 Brambleford Lane Suite 410<br>Cedarmoor Hollow, CA 90817<br>(805) 555-0142</div>
</article>

<article class="piece fax" style="left:552px;top:16px">
  <div class="brand">Brindle Terra</div>
  <table>
    <tr><td>To</td><td class="f"></td><td>From</td><td class="f"></td></tr>
    <tr><td>Fax</td><td class="f"></td><td>Pages</td><td class="f"></td></tr>
    <tr><td>Phone</td><td class="f"></td><td>Date</td><td class="f"></td></tr>
    <tr><td>Re</td><td class="f"></td><td>CC</td><td class="f"></td></tr>
  </table>
  <div class="checks">☐ Urgent ☐ For Review ☐ Please Reply ☐ Please Recycle<br>Comments:</div>
  <div class="band">1738 Brambleford Lane Suite 410 · www.MeganThistleHomes.com</div>
</article>
<article class="piece fax" style="left:636px;top:16px">
  <div class="brand" style="left:28px">Brindle Terra</div>
  <table>
    <tr><td>To</td><td class="f"></td><td>From</td><td class="f"></td></tr>
    <tr><td>Fax</td><td class="f"></td><td>Pages</td><td class="f"></td></tr>
    <tr><td>Phone</td><td class="f"></td><td>Date</td><td class="f"></td></tr>
    <tr><td>Re</td><td class="f"></td><td>CC</td><td class="f"></td></tr>
  </table>
  <div class="checks">☐ Urgent ☐ For Review ☐ Please Reply ☐ Please Recycle<br>Comments:</div>
  <div class="band">1738 Brambleford Lane Suite 410 · Megan@BrindleTerraHomes.com</div>
</article>

<article class="piece slip" style="left:728px;top:27px">
  <div class="brand">Brindle Terra</div>
  <div class="tiny" style="position:absolute;right:4px;top:5px;color:#666;font-size:1.4px">1738 Brambleford Lane Suite 410<br>Cedarmoor Hollow, CA 90817</div>
  <div class="script">With Compliments</div>
  <div class="band"></div>
</article>
<article class="piece slip" style="left:723px;top:74px;width:49px;height:35px">
  <div class="brand" style="left:10px;top:5px">Brindle Terra</div>
  <div class="script" style="position:absolute;left:7px;top:15px;font-size:8px;color:#444">Thank you</div>
  <div class="band" style="height:2.5px"></div>
</article>
<article class="piece red-fill" style="left:778px;top:74px;width:48px;height:35px">
  <div class="tiny" style="position:absolute;left:6px;top:22px;color:#fff;font-size:1.4px">1738 Brambleford Lane Suite 410<br>www.MeganThistleHomes.com</div>
</article>

<div class="disc red-fill" style="left:843px;top:5px;width:58px;height:58px"><div class="brand light">Brindle Terra</div><div class="hub"></div><div class="url">www.MeganThistleHomes.com</div></div>
<article class="piece" style="left:895px;top:7px;width:57px;height:54px">
  <div class="red-fill" style="position:absolute;left:0;right:0;top:0;height:8px"></div>
  <div class="brand" style="position:absolute;left:4px;top:13px;font-size:4px">Brindle Terra</div>
  <div class="band" style="height:3px"></div>
</article>

<div class="disc red-fill" style="left:684px;top:129px;width:58px;height:58px"><div class="brand light">Brindle Terra</div><div class="hub"></div><div class="url">www.MeganThistleHomes.com</div></div>
<div class="disc" style="left:750px;top:129px;width:58px;height:58px;background:radial-gradient(circle,#3a3a3a,#111)"><div class="brand light">Brindle Terra</div><div class="hub"></div><div class="url">www.MeganThistleHomes.com</div></div>
<div class="disc" style="left:684px;top:191px;width:58px;height:58px;background:#fff"><div class="brand">Brindle Terra</div><div class="hub" style="border-color:#111"></div><div class="url" style="color:var(--red)">www.MeganThistleHomes.com</div></div>
<div class="disc red-fill" style="left:754px;top:191px;width:58px;height:58px;border:2px solid #fff"><div class="brand light">Brindle Terra</div><div class="hub"></div><div class="url">www.MeganThistleHomes.com</div></div>

<article class="piece red-fill" style="left:825px;top:143px;width:59px;height:40px">
  <div class="brand light" style="position:absolute;left:4px;top:6px;font-size:4px">Brindle Terra</div>
  <div class="tiny" style="position:absolute;left:4px;bottom:5px;color:#fff;font-size:1.3px">1738 Brambleford Lane Suite 410, CA 90817</div>
</article>
<article class="piece" style="left:825px;top:197px;width:59px;height:40px">
  <div class="brand" style="position:absolute;left:4px;top:6px;font-size:4px">Brindle Terra</div>
  <div class="band" style="height:3px"></div>
</article>

<article class="piece" style="left:477px;top:136px;width:128px;height:77px;border-left:4px solid #333;border-right:4px solid #333">
  <div class="red-fill" style="position:absolute;left:8px;bottom:2px;width:52px;height:26px;clip-path:polygon(0 20%,100% 0,100% 100%,0 100%)"></div>
  <div class="red-fill" style="position:absolute;right:8px;bottom:2px;width:52px;height:26px;clip-path:polygon(0 0,100% 20%,100% 100%,0 100%)"></div>
</article>

<div class="magnet" style="left:488px;top:224px;width:20px;height:20px;background:#fff"><span class="brand">Brindle</span></div>
<div class="magnet red-fill" style="left:513px;top:224px;width:20px;height:20px"></div>
<div class="magnet" style="left:538px;top:224px;width:20px;height:20px;background:#1e1e1e"></div>
<div class="magnet" style="left:566px;top:224px;width:20px;height:20px;background:#fff"><span class="brand">Brindle</span></div>

<article class="piece slide" style="left:1008px;top:13px">
  <div class="brand" style="position:absolute;left:0;right:0;top:18px;text-align:center;font-size:9px">Brindle Terra</div>
  <div style="position:absolute;left:0;right:0;top:40px;text-align:center;font-size:3px;color:#333;line-height:4px">Welcome to Our<br><b style="color:var(--red);font-size:3.6px">Presentation Name</b><br>Description</div>
  <div class="band">www.MeganThistleHomes.com</div>
</article>
<article class="piece slide" style="left:1107px;top:13px">
  <h3>Heading Here</h3><h4>Sub Heading</h4>
  <div class="thumb" role="img" aria-label="Team photo" style="left:5px"></div>
  <div class="thumb" role="img" aria-label="Team photo" style="left:26px"></div>
  <div class="thumb" role="img" aria-label="Team photo" style="left:47px"></div>
  <div class="thumb" role="img" aria-label="Team photo" style="left:68px"></div>
  <div class="col" style="left:5px;top:36px"><b>Team member1</b>Title</div>
  <div class="col" style="left:26px;top:36px"><b>Team member2</b>Title</div>
  <div class="col" style="left:47px;top:36px"><b>Team member3</b>Title</div>
  <div class="col" style="left:68px;top:36px"><b>Team member4</b>Title</div>
  <div class="band">www.MeganThistleHomes.com</div>
</article>
<article class="piece slide" style="left:1008px;top:89px">
  <h3>Heading Here</h3><h4>Sub Heading</h4>
  <div class="col" style="left:5px;top:16px;width:38px"><b>Group1</b>Short notes about this group.<br><b>Group2</b>Short notes about this group.<br><b>Group3</b>Short notes about this group.</div>
  <div class="col" style="left:48px;top:16px;width:38px"><b>Group4</b>Short notes about this group.<br><b>Group5</b>Short notes about this group.<br><b>Group6</b>Short notes about this group.</div>
  <div class="band">www.MeganThistleHomes.com</div>
</article>
<article class="piece slide" style="left:1107px;top:89px">
  <h3>Heading Here</h3><h4>Sub Heading</h4>
  <svg style="position:absolute;left:6px;top:16px" width="42" height="34" viewBox="0 0 42 34">
    <line x1="1" y1="0" x2="1" y2="33" stroke="#999" stroke-width=".4"/>
    <line x1="1" y1="33" x2="42" y2="33" stroke="#999" stroke-width=".4"/>
    <rect x="4" y="4" width="5" height="29" fill="#a3121f"/>
    <rect x="11" y="9" width="5" height="24" fill="#a3121f"/>
    <rect x="18" y="12" width="5" height="21" fill="#a3121f"/>
    <rect x="25" y="16" width="5" height="17" fill="#a3121f"/>
    <rect x="32" y="22" width="5" height="11" fill="#a3121f"/>
  </svg>
  <div class="col" style="left:54px;top:17px;width:32px">Key figures for the quarter show steady growth across all listing types.</div>
  <div class="band">www.MeganThistleHomes.com</div>
</article>
<article class="piece slide" style="left:1008px;top:166px">
  <h3>Heading Here</h3><h4>Sub Heading</h4>
  <div class="col" style="left:5px;top:16px;width:44px">A brief overview of market share by neighborhood, drawn from this year's closed sales and active listings across the region.</div>
  <svg style="position:absolute;left:58px;top:17px" width="24" height="24" viewBox="-12 -12 24 24">
    <circle r="11" fill="#a3121f"/>
    <path d="M0 0 L0 -11 A11 11 0 0 1 10.5 -3.4 Z" fill="#555"/>
    <path d="M0 0 L10.5 -3.4 A11 11 0 0 1 6.5 8.9 Z" fill="#d9d9d9"/>
  </svg>
  <div class="band">www.MeganThistleHomes.com</div>
</article>
<article class="piece slide red-fill" style="left:1107px;top:166px">
  <div style="position:absolute;left:0;right:0;top:18px;text-align:center;color:#fff;font-size:14px;line-height:14px;font-weight:400">Thanks</div>
  <div style="position:absolute;left:0;right:0;top:33px;text-align:center;color:#fff;font-size:7px">For Coming</div>
  <div class="tiny" style="position:absolute;left:0;right:0;bottom:3px;text-align:center;color:#fff;font-size:1.4px;white-space:nowrap">1738 Brambleford Lane Suite 410, Cedarmoor Hollow, CA 90817 · Megan@BrindleTerraHomes.com</div>
</article>

</body>
</html>
```